ALL TEXT GRAPHICS TM May 2025 for Instagram

We are looking for a series of social media graphics for Instagram (new size: 4:5 (1080 x 1350 pixels) ratio that are ALL TEXT. We want the following quotes below on each graphic; one quote per graphic. AND, In very small letters at the bottom of each graphic, add @TovaMarshOnline
The look and feel of these graphics should be complimentary to the color palette attached below; but keep them simple. But the design is up to you; at the end of this document, I provided various samples of all text graphics that I like as examples.
Target Market(s)
women looking to lose weight
Look and feel

```html
<!DOCTYPE html>
<html lang="en">
<head>
<meta charset="utf-8">
<title>All Text Graphics – Tova Marsh</title>
<link rel="stylesheet" href="https://fonts.googleapis.com/css2?family=Oswald:wght@600&family=Montserrat:wght@600&display=swap">
<style>
  :root {
    --canvas-bg: #000000;
    --card-bg: #ffffff;
    --pink-top: #ff6fb5;
    --pink-bottom: #e6318e;
    --text: #ffffff;
  }
  * { margin: 0; padding: 0; box-sizing: border-box; }
  html, body { width: 1200px; height: 606px; overflow: hidden; background: var(--canvas-bg); }
  .series {
    position: relative;
    width: 1200px;
    height: 606px;
    display: grid;
    grid-template-columns: repeat(5, 221px);
    grid-template-rows: repeat(2, 276px);
    column-gap: 14px;
    row-gap: 17px;
    padding: 18px 0 0 20px;
  }
  .post {
    position: relative;
    width: 221px;
    height: 276px;
    background: var(--card-bg);
    overflow: hidden;
  }
  .post__wave {
    position: absolute;
    inset: 0;
    width: 221px;
    height: 276px;
  }
  .post__quote {
    position: absolute;
    left: 21px;
    right: 21px;
    top: 24px;
    text-align: center;
    font-family: "Oswald", "Arial Narrow", sans-serif;
    font-weight: 600;
    font-size: 19.5px;
    line-height: 24.9px;
    letter-spacing: -0.3px;
    color: var(--text);
    transform: scaleX(0.9);
  }
  .post__quote--tight { top: 20px; }
  .post__quote--low { top: 33px; }
  .post__handle {
    position: absolute;
    left: 0;
    right: 0;
    top: 242px;
    text-align: center;
    font-family: "Montserrat", Arial, sans-serif;
    font-weight: 600;
    font-size: 8.5px;
    letter-spacing: 0.5px;
    color: var(--text);
  }
</style>
</head>
<body>
<svg width="0" height="0" style="position:absolute" aria-hidden="true">
  <defs>
    <linearGradient id="pinkFill" x1="0" y1="0" x2="0.35" y2="1">
      <stop offset="0" stop-color="var(--pink-top)"/>
      <stop offset="1" stop-color="var(--pink-bottom)"/>
    </linearGradient>
    <symbol id="wavyPanel" viewBox="0 0 221 276">
      <path fill="url(#pinkFill)" d="
        M 37 0 L 200 0
        C 184 10, 184 18, 200 28
        C 216 38, 216 46, 200 55
        C 184 65, 184 73, 200 83
        C 216 93, 216 101, 200 110
        C 184 120, 184 128, 200 138
        C 216 148, 216 156, 200 165
        C 184 175, 184 183, 200 193
        C 216 203, 216 211, 200 220
        C 184 230, 184 238, 200 248
        C 216 258, 216 266, 200 276
        L 37 276
        C 21 266, 21 258, 37 248
        C 53 238, 53 230, 37 220
        C 21 211, 21 203, 37 193
        C 53 183, 53 175, 37 165
        C 21 156, 21 148, 37 138
        C 53 128, 53 120, 37 110
        C 21 101, 21 93, 37 83
        C 53 73, 53 65, 37 55
        C 21 46, 21 38, 37 28
        C 53 18, 53 10, 37 0 Z"/>
    </symbol>
  </defs>
</svg>

<main class="series">
  <article class="post">
    <svg class="post__wave" aria-hidden="true"><use href="#wavyPanel"/></svg>
    <p class="post__quote post__quote--tight">Your belly<br>isn’t fat… it’s<br>hormonal. And<br>here’s<br>how to fix it.<br>Comment HORMONES<br>if nothing is<br>working.</p>
    <p class="post__handle">@TovaMarshOnline</p>
  </article>
  <article class="post">
    <svg class="post__wave" aria-hidden="true"><use href="#wavyPanel"/></svg>
    <p class="post__quote">Flat tummy in<br>your 40s?<br>It’s still<br>possible! Comment<br>BYE BELLY<br>to get the<br>10 secrets to a<br>flatter tummy</p>
    <p class="post__handle">@TovaMarshOnline</p>
  </article>
  <article class="post">
    <svg class="post__wave" aria-hidden="true"><use href="#wavyPanel"/></svg>
    <p class="post__quote">Flat tummy in<br>your 40s?<br>It’s still<br>possible! Comment<br>BYE BELLY<br>to get the<br>10 secrets to a<br>flatter tummy</p>
    <p class="post__handle">@TovaMarshOnline</p>
  </article>
  <article class="post">
    <svg class="post__wave" aria-hidden="true"><use href="#wavyPanel"/></svg>
    <p class="post__quote">Flat tummy in<br>your 40s?<br>It’s still<br>possible! Comment<br>BYE BELLY<br>to get the<br>10 secrets to a<br>flatter tummy</p>
    <p class="post__handle">@TovaMarshOnline</p>
  </article>
  <article class="post">
    <svg class="post__wave" aria-hidden="true"><use href="#wavyPanel"/></svg>
    <p class="post__quote">Flat tummy in<br>your 40s?<br>It’s still<br>possible! Comment<br>BYE BELLY<br>to get the<br>10 secrets to a<br>flatter tummy</p>
    <p class="post__handle">@TovaMarshOnline</p>
  </article>

  <article class="post">
    <svg class="post__wave" aria-hidden="true"><use href="#wavyPanel"/></svg>
    <p class="post__quote">Flat tummy in<br>your 40s?<br>It’s still<br>possible! Comment<br>BYE BELLY<br>to get the<br>10 secrets to a<br>flatter tummy</p>
    <p class="post__handle">@TovaMarshOnline</p>
  </article>
  <article class="post">
    <svg class="post__wave" aria-hidden="true"><use href="#wavyPanel"/></svg>
    <p class="post__quote">Flat tummy in<br>your 40s?<br>It’s still<br>possible! Comment<br>BYE BELLY<br>to get the<br>10 secrets to a<br>flatter tummy</p>
    <p class="post__handle">@TovaMarshOnline</p>
  </article>
  <article class="post">
    <svg class="post__wave" aria-hidden="true"><use href="#wavyPanel"/></svg>
    <p class="post__quote post__quote--low">This 90-day plan<br>helped<br>women over 40<br>slim down,<br>get a tiny waist<br>and feel sexy<br>again.<br>You’re next.</p>
    <p class="post__handle">@TovaMarshOnline</p>
  </article>
  <article class="post">
    <svg class="post__wave" aria-hidden="true"><use href="#wavyPanel"/></svg>
    <p class="post__quote post__quote--tight">The stubborn<br>belly fat<br>after 40?<br>It’s not about<br>calories;<br>it’s about your<br>hormones.<br>Here is the fix!</p>
    <p class="post__handle">@TovaMarshOnline</p>
  </article>
  <article class="post">
    <svg class="post__wave" aria-hidden="true"><use href="#wavyPanel"/></svg>
    <p class="post__quote">What worked<br>in your 30s<br>won’t<br>work now. Here’s<br>what<br>actually does.<br>Drop 30 Pounds<br>in 3 Months.</p>
    <p class="post__handle">@TovaMarshOnline</p>
  </article>
</main>
</body>
</html>
```